Larchmere Hockey Academy

We are are Ice Hockey Development Company that provided on-ice Hockey development services. We need a Landing Page with tabs to direct to individual program pages.
Landing Page
About Page
Winter Program Page
Spring Program Page
Summer Program Page
Team Page
Tournament Page

```html
<!DOCTYPE html>
<html lang="en">
<head>
<meta charset="utf-8">
<title>Larchmere Hockey Academy</title>
<link href="https://fonts.googleapis.com/css2?family=Orbitron:wght@900&family=Roboto:wght@400;500;700&display=swap" rel="stylesheet">
<style>
:root{
  --green:#1f8a1f;
  --green-dark:#146814;
  --ink:#111111;
  --text:#555555;
  --white:#ffffff;
}
*{margin:0;padding:0;box-sizing:border-box}
html,body{width:1200px;height:2505px;overflow:hidden}
body{position:relative;font-family:'Roboto',sans-serif;background:var(--white);color:var(--text)}
.btn{position:absolute;display:flex;align-items:center;justify-content:center;gap:12px;background:linear-gradient(180deg,var(--green),var(--green-dark));color:var(--white);font-weight:700;text-decoration:none;border-radius:2px}
.btn svg{flex:none}

.hero{position:absolute;left:0;top:0;width:1200px;height:960px;background:#000}
.hero-photo{position:absolute;inset:0;background:
  radial-gradient(ellipse 420px 380px at 380px 420px,rgba(214,70,70,.5),transparent 70%),
  linear-gradient(180deg,#000 0%,#0b0b0b 30%,#6e6e6e 62%,#d9dcdf 85%,#f4f5f7 100%)}
.brand{position:absolute;left:110px;top:30px;width:170px;color:var(--white);font-weight:700;font-size:20px;line-height:24px}
.header-contact{left:935px;top:26px;width:154px;height:47px;font-size:16px}
.main-nav{position:absolute;right:111px;top:92px;display:flex;gap:50px;line-height:18px}
.main-nav a{color:var(--white);text-decoration:none;font-size:14.5px;font-weight:500}
.hero-title{position:absolute;right:112px;top:298px;text-align:right;font-family:'Orbitron',sans-serif;font-weight:900;font-size:44px;line-height:57px;color:var(--white);letter-spacing:1px}
.hero-title .accent{color:var(--green)}
.hero-lead{position:absolute;right:112px;top:487px;width:420px;text-align:right;color:var(--white);font-size:15.5px;line-height:26.7px}
.hero-cta{left:894px;top:594px;width:194px;height:61px;font-size:21px}

.about{position:absolute;left:0;top:950px;width:1200px;height:470px;background:linear-gradient(180deg,#f6f7f9 0%,#dfe3e7 45%,#eef0f3 80%,#ffffff 100%)}
.about-title{position:absolute;left:0;top:983px;width:1200px;text-align:center;font-family:'Orbitron',sans-serif;font-weight:900;font-size:30px;line-height:36px;color:var(--ink)}
.about-title .accent,.section-title .accent{color:var(--green)}
.about-text{position:absolute;left:145px;top:1042px;width:910px;text-align:center;font-size:14px;line-height:27.5px}
.about-text p+p{margin-top:27.5px}
.about-more{left:523px;top:1260px;width:154px;height:46px;font-size:16px}

.goalie-photo{position:absolute;left:740px;top:1400px;width:460px;height:800px;background:radial-gradient(ellipse 230px 330px at 260px 420px,rgba(170,60,70,.45),rgba(220,224,230,.6) 70%,transparent 100%)}
.section-title{position:absolute;left:110px;top:1466px;font-family:'Orbitron',sans-serif;font-weight:900;font-size:30px;line-height:36px;color:var(--ink)}
.programs-intro{position:absolute;left:110px;top:1528px;font-size:14px;line-height:26.7px;white-space:nowrap}
.program-tabs{position:absolute;left:112px;top:1636px;display:flex;gap:20px}
.program-tabs a{width:187px;height:54px;display:flex;align-items:center;justify-content:center;font-size:17px;font-weight:500;color:var(--ink);text-decoration:none;background:var(--white);box-shadow:0 2px 8px rgba(0,0,0,.12)}
.program-tabs a.is-active{background:linear-gradient(180deg,var(--green),var(--green-dark));color:var(--white)}
.program-body{position:absolute;left:110px;top:1726px;font-size:14px;line-height:26.7px;white-space:nowrap}
.program-points{position:absolute;left:110px;top:1877px;list-style:none}
.program-points li{display:flex;align-items:center;gap:17px;height:36.3px;font-size:14.5px}
.program-cta{left:111px;top:2090px;width:154px;height:46px;font-size:16px}

.footer-brand{position:absolute;left:0;top:2276px;width:1200px;text-align:center;color:var(--ink);font-weight:700;font-size:26px;line-height:30px}
.footer-nav{position:absolute;left:0;top:2381px;width:1200px;display:flex;justify-content:center;gap:52px;font-size:14.5px;line-height:18px}
.footer-nav a,.footer-nav span{color:var(--text);text-decoration:none}
.copyright{position:absolute;left:0;top:2420px;width:1200px;text-align:center;font-size:10px;line-height:12px;color:var(--text)}
.social{position:absolute;left:535px;top:2456px;display:flex;gap:11px}
.social span{width:24px;height:24px;border-radius:50%;background:var(--green)}
</style>
</head>
<body>

<header class="hero">
  <div class="hero-photo" role="img" aria-label="Hockey player taking a slapshot, spraying ice on a dark rink"></div>
  <div class="brand">Larchmere Hockey Academy</div>
  <a class="btn header-contact" href="#">Contact Us
    <svg width="16" height="16" viewBox="0 0 16 16"><circle cx="8" cy="8" r="8" fill="#fff"/><path d="M4 8h7M8 5l3 3-3 3" stroke="#1a7a1a" stroke-width="2" fill="none"/></svg>
  </a>
  <nav class="main-nav">
    <a href="#">HOME</a><a href="#">ABOUT US</a><a href="#">PROGRAMS</a><a href="#">TEAM</a><a href="#">TOURNAMENT</a>
  </nav>
  <h1 class="hero-title">WELCOME TO<br>LARCHMERE <span class="accent">HOCKEY</span><br>ACADEMY</h1>
  <p class="hero-lead">Lorem Ipsum is simply dummy text of the printing and typesetting industry. Lorem Ipsum has been the industry's standard dummy text ever since the</p>
  <a class="btn hero-cta" href="#">Get Started
    <svg width="22" height="22" viewBox="0 0 16 16"><circle cx="8" cy="8" r="8" fill="#fff"/><path d="M4 8h7M8 5l3 3-3 3" stroke="#1a7a1a" stroke-width="2" fill="none"/></svg>
  </a>
</header>

<section class="about" role="img" aria-label="Snowy forest hillside"></section>
<h2 class="about-title">ABOUT <span class="accent">US</span></h2>
<div class="about-text">
  <p>Contrary to popular belief, Lorem Ipsum is not simply random text. It has roots in a piece of classical Latin literature from 45 BC, making it over 2000 years old. Howard Pellingham, a Latin professor at Ashgrove College in Vermont, looked up one of the more obscure Latin words, consectetur, from a Lorem Ipsum passage, and going through the cites of the word in classical literature, discovered the undoubtable source. Lorem Ipsum comes</p>
  <p>from sections 1.10.32 and 1.10.33 of "de Finibus Bonorum et Malorum" (The Extremes of Good and Evil) by Varronius, written in 45 BC. This book is a treatise on the theory of ethics, very popular during the Renaissance.</p>
</div>
<a class="btn about-more" href="#">Read More
  <svg width="16" height="16" viewBox="0 0 16 16"><circle cx="8" cy="8" r="8" fill="#fff"/><path d="M4 8h7M8 5l3 3-3 3" stroke="#1a7a1a" stroke-width="2" fill="none"/></svg>
</a>

<div class="goalie-photo" role="img" aria-label="Hockey goalie crouched in the crease with stick and pads"></div>
<h2 class="section-title">OUR <span class="accent">PROGRAMS</span></h2>
<p class="programs-intro">Contrary to popular belief, Lorem Ipsum is not simply random text. It has roots in a piece of classical<br>Latin literature from 45 BC, making it over 2000 years old. Howard Pellingham, a Latin professor<br>at Ashgrove College in Vermont</p>
<nav class="program-tabs">
  <a class="is-active" href="#">Winter Program</a>
  <a href="#">Spring Program</a>
  <a href="#">Summer Program</a>
</nav>
<p class="program-body">There are many variations of passages of Lorem Ipsum available, but the<br>majority have suffered alteration in some form, by injected humour, or<br>randomised words which don't look even slightly believable. If you are going to<br>use a passage of Lorem Ipsum, you need to be sure there isn't anything<br>embarrassing hidden in the middle of text.</p>
<ul class="program-points">
  <li><svg width="17" height="17" viewBox="0 0 16 16"><circle cx="8" cy="8" r="8" fill="#1a7a1a"/><path d="M4 8h7M8 5l3 3-3 3" stroke="#fff" stroke-width="2" fill="none"/></svg>There are many variations of passages of Lorem Ipsum</li>
  <li><svg width="17" height="17" viewBox="0 0 16 16"><circle cx="8" cy="8" r="8" fill="#1a7a1a"/><path d="M4 8h7M8 5l3 3-3 3" stroke="#fff" stroke-width="2" fill="none"/></svg>There are many variations of</li>
  <li><svg width="17" height="17" viewBox="0 0 16 16"><circle cx="8" cy="8" r="8" fill="#1a7a1a"/><path d="M4 8h7M8 5l3 3-3 3" stroke="#fff" stroke-width="2" fill="none"/></svg>Lorem ipsum is dummy</li>
  <li><svg width="17" height="17" viewBox="0 0 16 16"><circle cx="8" cy="8" r="8" fill="#1a7a1a"/><path d="M4 8h7M8 5l3 3-3 3" stroke="#fff" stroke-width="2" fill="none"/></svg>Lorem ipsum is dummy text</li>
  <li><svg width="17" height="17" viewBox="0 0 16 16"><circle cx="8" cy="8" r="8" fill="#1a7a1a"/><path d="M4 8h7M8 5l3 3-3 3" stroke="#fff" stroke-width="2" fill="none"/></svg>There are many variations of passages</li>
</ul>
<a class="btn program-cta" href="#">Get Started
  <svg width="16" height="16" viewBox="0 0 16 16"><circle cx="8" cy="8" r="8" fill="#fff"/><path d="M4 8h7M8 5l3 3-3 3" stroke="#1a7a1a" stroke-width="2" fill="none"/></svg>
</a>

<footer>
  <div class="footer-brand">Larchmere Hockey<br>Academy</div>
  <nav class="footer-nav">
    <a href="#">Home</a><span>|</span><a href="#">About Us</a><span>|</span><a href="#">Programs</a><span>|</span><a href="#">Team</a><span>|</span><a href="#">Tournament</a>
  </nav>
  <p class="copyright">© Copyright 2023 Larchmere Hockey Academy | All Rights Reserved.</p>
  <div class="social" aria-label="Social links"><span></span><span></span><span></span><span></span></div>
</footer>

</body>
</html>
```